Business Card Design for a Handbags business

We are modernising our handbags website (see attached file for new front page) and are in need of a modern business card and a related design we can use on a small marquee at the markets, on letterhead, emails etc.

As the leather handbags we mostly import are from Italy, we want a smart modern European feel to the design. We are currently thinking about changing the name of the business from Larkmoor Handbags (see www.larkmoorhandbags.com.au) to Vintessa Handbags. Also open to other suggestions you may have that communicates the European influence and quality.

Target Market(s)

25-65 year old women (and some men)

Industry/Entity Type

Business

Contact Information for Business Card

Single or double sided - whichever creates more of an impact

Font styles to use
Serif
Sans Serif

Requirements
Must have
• Clean crisp look, slightly Italian or European look and feel to reflect where the handbags are imported from
Nice to have
• open to ideas

```html
<!DOCTYPE html>
<html lang="en">
<head>
<meta charset="utf-8">
<title>Larkmoor Handbags – Business Card</title>
<link rel="stylesheet" href="https://fonts.googleapis.com/css2?family=Almendra:wght@400&display=swap">
<style>
  :root {
    --ink: #2a2929;
    --paper: #ffffff;
    --backdrop: #eceeee;
  }
  * { margin: 0; padding: 0; box-sizing: border-box; }
  html, body {
    width: 1200px;
    height: 934px;
    overflow: hidden;
    background: var(--backdrop);
  }
  .card {
    position: absolute;
    left: 148px;
    top: 166px;
    width: 907px;
    height: 560px;
    background: var(--paper);
    font-family: "Almendra", Georgia, serif;
    color: var(--ink);
  }
  .card__band {
    position: absolute;
    left: 0; top: 0;
    width: 100%;
    height: 163px;
    background: var(--ink);
  }
  .card__band-stripe {
    position: absolute;
    left: 0; top: 169px;
    width: 100%;
    height: 15px;
    background: var(--ink);
  }
  .line {
    position: absolute;
    left: 0;
    width: 100%;
    text-align: center;
    white-space: nowrap;
    line-height: 40px;
    height: 40px;
  }
  .brand__name     { top: 188px; font-size: 32px; letter-spacing: 0.5px; }
  .brand__amp      { top: 218px; font-size: 28px; }
  .brand__tagline  { top: 250px; font-size: 32px; }
  .brand__rule {
    position: absolute;
    left: 333px; top: 302px;
    width: 239px;
    height: 3px;
    background: var(--ink);
  }
  .contact__person { top: 342px; font-size: 32px; letter-spacing: 1px; }
  .contact__line {
    position: absolute;
    left: 325px;
    display: flex;
    align-items: center;
    gap: 12px;
    white-space: nowrap;
  }
  .contact__line--phone { top: 403px; height: 40px; font-size: 32px; letter-spacing: 2px; }
  .contact__line--place { top: 454px; height: 32px; font-size: 24px; letter-spacing: 0.5px; }
  .contact__icon { flex: none; fill: var(--ink); }
</style>
</head>
<body>
  <section class="card">
    <div class="card__band"></div>
    <div class="card__band-stripe"></div>

    <p class="line brand__name">Larkmoor Handbags</p>
    <p class="line brand__amp">&amp;</p>
    <p class="line brand__tagline">Accessories</p>
    <div class="brand__rule"></div>

    <p class="line contact__person">Clara Westbrook</p>

    <p class="contact__line contact__line--phone">
      <svg class="contact__icon" width="19" height="29" viewBox="0 0 22 34" aria-hidden="true">
        <path d="M4 0h14a4 4 0 0 1 4 4v26a4 4 0 0 1-4 4H4a4 4 0 0 1-4-4V4a4 4 0 0 1 4-4zm-1 5v21h16V5zm8 23a2 2 0 1 0 0 4 2 2 0 0 0 0-4z" fill-rule="evenodd"/>
      </svg>
      <span>0412 555 308</span>
    </p>

    <p class="contact__line contact__line--place">
      <svg class="contact__icon" width="19" height="29" viewBox="0 0 22 34" aria-hidden="true">
        <path d="M11 0a11 11 0 0 1 11 11c0 8-11 23-11 23S0 19 0 11A11 11 0 0 1 11 0zm0 6a5 5 0 1 0 0 10 5 5 0 0 0 0-10z" fill-rule="evenodd"/>
      </svg>
      <span>Larkfield, Ashvale</span>
    </p>
  </section>
</body>
</html>
```